Business Card Design

we need a bussiness card for the transport company called Varlen Transport
name of contact person that should display on card is Marek Tolleson contact no 0481620357
we do the dry goods and frozen deliveries in melbourne every day
happy to beat any quote

Industry/Entity Type

Business

Contact Information for Business Card

Varlen transport
Marek tolleson
mob 0481620357
contact us for any refrigerator or dry goods delivery
deliver all over melbourne

```html
<!DOCTYPE html>
<html lang="en">
<head>
<meta charset="utf-8">
<title>Varlen Transport – Business Card Concepts</title>
<link href="https://fonts.googleapis.com/css2?family=Open+Sans:wght@400;600;700&display=swap" rel="stylesheet">
<style>
  :root {
    --sheet: #ffffff;
    --label: #111111;
    --dark-top: #4a0504;
    --dark-bottom: #2a0000;
    --back-top: #2c0000;
    --back-bottom: #5c0503;
    --back-alt-top: #360101;
    --back-alt-bottom: #6c0702;
    --band-red: #8a0b05;
    --band-ink: #3c0000;
    --faint-mark: #7e0b06;
    --bright-bg: #8e0b02;
    --bright-band: #680600;
    --white: #ffffff;
  }
  html, body {
    margin: 0;
    padding: 0;
    width: 1200px;
    height: 874px;
    overflow: hidden;
    background: var(--sheet);
  }
  .sheet {
    position: relative;
    width: 1200px;
    height: 874px;
    font-family: "Open Sans", Arial, sans-serif;
  }
  .concept-label {
    position: absolute;
    margin: 0;
    font-size: 18px;
    font-weight: 400;
    color: var(--label);
    line-height: 1;
  }
  .card {
    position: absolute;
    width: 487px;
    height: 314px;
    display: block;
  }
  .card text { font-family: "Open Sans", Arial, sans-serif; }
  .tagline { font-weight: 700; font-size: 30px; }
  .promise { font-weight: 600; font-size: 24px; }
  .contact-name { font-weight: 700; font-size: 18px; }
  .contact-phone { font-weight: 400; font-size: 13px; }
  .brand-name { font-weight: 400; }
</style>
</head>
<body>
<main class="sheet">

  <p class="concept-label" style="left:106px; top:77px;">BC 1</p>
  <p class="concept-label" style="left:628px; top:77px;">BC 1</p>
  <p class="concept-label" style="left:106px; top:445px;">BC 2</p>
  <p class="concept-label" style="left:628px; top:445px;">BC 2</p>

  <!-- BC 1 front -->
  <svg class="card card-front card-dark" style="left:96px; top:98px;" viewBox="0 0 597 385" aria-label="Varlen Transport business card, front, dark version">
    <defs>
      <linearGradient id="dark-front-bg" x1="0" y1="0" x2="1" y2="1">
        <stop offset="0" stop-color="var(--dark-top)"/>
        <stop offset="1" stop-color="var(--dark-bottom)"/>
      </linearGradient>
      <filter id="band-shadow" x="-20%" y="-50%" width="140%" height="200%">
        <feDropShadow dx="4" dy="8" stdDeviation="6" flood-color="#000" flood-opacity="0.55"/>
      </filter>
    </defs>
    <rect class="card-surface" width="597" height="385" fill="url(#dark-front-bg)"/>
    <g class="tagline-band" transform="translate(0,198) rotate(-20)" filter="url(#band-shadow)">
      <rect x="-30" y="-31" width="545" height="62" rx="31" fill="var(--band-red)"/>
      <text class="tagline" x="45" y="11" fill="var(--band-ink)">Dry &amp; frozen goods deliveries</text>
    </g>
    <g class="promise-band" transform="translate(0,278) rotate(-20)" filter="url(#band-shadow)">
      <rect x="-30" y="-27" width="445" height="54" rx="27" fill="var(--band-red)"/>
      <text class="promise" x="75" y="9" fill="var(--band-ink)">We will beat any quote!</text>
    </g>
    <g class="contact" fill="var(--band-red)" text-anchor="end">
      <text class="contact-name" x="390" y="313">Marek Tolleson</text>
      <text class="contact-phone" x="390" y="333">m: 0481620357</text>
    </g>
    <rect class="divider" x="401" y="225" width="2" height="110" fill="var(--band-red)"/>
    <g class="brand-lockup" fill="var(--band-red)" text-anchor="middle">
      <circle cx="482" cy="222" r="34"/>
      <text class="brand-name" x="482" y="301" font-size="28">VARLEN</text>
      <text class="brand-name" x="482" y="335" font-size="20">TRANSPORT</text>
    </g>
  </svg>

  <!-- BC 1 back -->
  <svg class="card card-back" style="left:615px; top:98px;" viewBox="0 0 597 385" aria-label="Varlen Transport business card, back">
    <defs>
      <linearGradient id="back-bg" x1="0" y1="0" x2="0" y2="1">
        <stop offset="0" stop-color="var(--back-top)"/>
        <stop offset="1" stop-color="var(--back-bottom)"/>
      </linearGradient>
    </defs>
    <rect class="card-surface" width="597" height="385" fill="url(#back-bg)"/>
    <g class="brand-lockup brand-lockup-large" fill="var(--faint-mark)" text-anchor="middle">
      <circle cx="298" cy="135" r="62"/>
      <text class="brand-name" x="300" y="275" font-size="52">VARLEN</text>
      <text class="brand-name" x="300" y="332" font-size="38">TRANSPORT</text>
    </g>
  </svg>

  <!-- BC 2 back -->
  <svg class="card card-back" style="left:96px; top:465px;" viewBox="0 0 597 385" aria-label="Varlen Transport business card, back, alternate">
    <defs>
      <linearGradient id="back-alt-bg" x1="0" y1="0" x2="0" y2="1">
        <stop offset="0" stop-color="var(--back-alt-top)"/>
        <stop offset="1" stop-color="var(--back-alt-bottom)"/>
      </linearGradient>
    </defs>
    <rect class="card-surface" width="597" height="385" fill="url(#back-alt-bg)"/>
    <g class="brand-lockup brand-lockup-large" fill="var(--faint-mark)" text-anchor="middle">
      <circle cx="298" cy="135" r="62"/>
      <text class="brand-name" x="300" y="275" font-size="52">VARLEN</text>
      <text class="brand-name" x="300" y="332" font-size="38">TRANSPORT</text>
    </g>
  </svg>

  <!-- BC 2 front -->
  <svg class="card card-front card-bright" style="left:615px; top:465px;" viewBox="0 0 597 385" aria-label="Varlen Transport business card, front, bright version">
    <defs>
      <filter id="band-shadow-bright" x="-20%" y="-50%" width="140%" height="200%">
        <feDropShadow dx="4" dy="8" stdDeviation="6" flood-color="#000" flood-opacity="0.45"/>
      </filter>
    </defs>
    <rect class="card-surface" width="597" height="385" fill="var(--bright-bg)"/>
    <g class="tagline-band" transform="translate(0,198) rotate(-20)" filter="url(#band-shadow-bright)">
      <rect x="-30" y="-31" width="545" height="62" rx="31" fill="var(--bright-band)"/>
      <text class="tagline" x="45" y="11" fill="var(--white)">Dry &amp; frozen goods deliveries</text>
    </g>
    <g class="promise-band" transform="translate(0,278) rotate(-20)" filter="url(#band-shadow-bright)">
      <rect x="-30" y="-27" width="445" height="54" rx="27" fill="var(--bright-band)"/>
      <text class="promise" x="75" y="9" fill="var(--white)">We will beat any quote!</text>
    </g>
    <g class="contact" fill="var(--white)" text-anchor="end">
      <text class="contact-name" x="390" y="313">Marek Tolleson</text>
      <text class="contact-phone" x="390" y="333">m: 0481620357</text>
    </g>
    <rect class="divider" x="401" y="225" width="2" height="110" fill="var(--white)"/>
    <g class="brand-lockup" fill="var(--white)" text-anchor="middle">
      <circle cx="482" cy="222" r="34"/>
      <text class="brand-name" x="482" y="301" font-size="28">VARLEN</text>
      <text class="brand-name" x="482" y="335" font-size="20">TRANSPORT</text>
    </g>
  </svg>

</main>
</body>
</html>
```